7 P's for Healthcare Companies - Textbook Graphic

Can you create a graphic for me for a medical textbook? The goal is to show 7 critical features of a healthcare startup and the audience is physicians with limited business backgrounds.

Please include a picture of young, male emergency physician in the middle of the graphic. Show them evaluating an idea. Can you surround the physician with bold writing for the seven components, and use brief descriptions and simple images or graphics to illustrate the point?

The image should be somewhat formal, but it's OK to be lighthearded.

The seven P's and brief descriptions include the following:
Product: what is their market solution?
(Intellectual) Property: do they have a patent or trademark?
Product Clearance: how will they get QRB approval and TPW clearance?
Payment: how will they make money?
Pilots: have they applied their product in a healthcare setting?
Physician and Patient feedback: Do doctors and patients like their product?
Publication: do they have evidence their product works?

More detail and information is available at this website: https://brenvolt.com/blog/uncategorized/healthcare-framework/

I will need to own this image

```html
<!DOCTYPE html>
<html lang="en">
<head>
<meta charset="utf-8">
<title>7 P's for Healthcare Companies</title>
<link rel="stylesheet" href="https://fonts.googleapis.com/css2?family=Archivo+Black&display=swap">
<style>
  :root {
    --ink: #1e2b3c;
    --paper: #e6e6e6;
    --figure-top: #cfd3d8;
    --figure-bottom: #bcc3cb;
  }
  html, body {
    margin: 0;
    padding: 0;
    width: 1200px;
    height: 1200px;
    overflow: hidden;
    background: var(--paper);
  }
  .framework {
    display: block;
    width: 1200px;
    height: 1200px;
  }
  .ring { fill: none; stroke: var(--ink); stroke-width: 14; }
  .node { fill: var(--paper); stroke: var(--ink); stroke-width: 14; }
  .icon { fill: none; stroke: var(--ink); stroke-width: 4.5; stroke-linecap: round; stroke-linejoin: round; }
  .icon .solid { fill: var(--ink); stroke: none; }
  .label { font-family: "Archivo Black", "Arial Black", sans-serif; fill: var(--ink); }
  .label-initial { font-size: 90px; }
  .label-rest { font-size: 19px; }
  .label-note { font-size: 8px; }
  .title { font-family: "Archivo Black", "Arial Black", sans-serif; fill: var(--ink); font-size: 160px; }
</style>
</head>
<body>
<svg class="framework" viewBox="0 0 1200 1200" xmlns="http://www.w3.org/2000/svg">
  <defs>
    <linearGradient id="figure-fill" x1="0" y1="0" x2="0" y2="1">
      <stop offset="0" stop-color="var(--figure-top)"/>
      <stop offset="1" stop-color="var(--figure-bottom)"/>
    </linearGradient>
  </defs>

  <!-- connecting ring -->
  <circle class="ring" cx="612" cy="621" r="354"/>

  <!-- central physician figure -->
  <rect class="physician" x="441" y="338" width="332" height="362" rx="40" fill="url(#figure-fill)"
        role="img" aria-label="Line drawing of a young male emergency physician in a coat and tie with a stethoscope, evaluating an idea"/>

  <text class="title" x="463" y="823" textLength="300" lengthAdjust="spacingAndGlyphs">7P’s</text>

  <!-- Publication -->
  <g class="step step-publication">
    <circle class="node" cx="461" cy="287" r="88"/>
    <g class="icon" transform="translate(461 287)">
      <path d="M-38 12 L-12 -22 L22 22 L-26 32 Z"/>
      <ellipse cx="5" cy="0" rx="14" ry="27" transform="rotate(-35 5 0)"/>
      <path d="M-38 12 Q-50 20 -42 32 Q-36 38 -26 32"/>
      <path d="M-14 30 L-4 50 Q0 56 8 50 L-2 30"/>
      <path d="M20 -38 Q42 -28 38 -4"/>
      <path d="M26 -52 Q58 -38 52 0"/>
    </g>
    <text class="label label-initial" x="396" y="171">P</text>
    <text class="label label-rest" x="454" y="172">UBLICATION</text>
  </g>

  <!-- Product -->
  <g class="step step-product">
    <circle class="node" cx="761" cy="287" r="88"/>
    <g class="icon" transform="translate(761 287)">
      <path d="M-48 4 L0 -14 L48 4 L0 22 Z"/>
      <path d="M-48 4 L-48 36 L0 56 L48 36 L48 4"/>
      <path d="M0 22 L0 56"/>
      <path d="M-48 4 L-56 -8 L-8 -26"/>
      <path d="M48 4 L56 -8 L8 -26"/>
      <circle cx="0" cy="-36" r="13"/>
      <path d="M-7 -20 L7 -20 M-6 -14 L6 -14"/>
      <path d="M0 -62 L0 -56 M-22 -54 L-18 -48 M22 -54 L18 -48 M-32 -38 L-26 -36 M32 -38 L26 -36"/>
    </g>
    <text class="label label-initial" x="735" y="171">P</text>
    <text class="label label-rest" x="764" y="172">RODUCT</text>
  </g>

  <!-- (Intellectual) Property -->
  <g class="step step-property">
    <circle class="node" cx="949" cy="519" r="88"/>
    <g class="icon" transform="translate(949 519)">
      <path d="M-38 -52 L34 -52 Q44 -52 44 -40 L44 48 Q44 58 34 58 L-40 58"/>
      <path d="M-38 -52 L-38 40"/>
      <path d="M34 -52 Q28 -52 28 -42 L50 -42 Q50 -52 44 -52"/>
      <path d="M-50 40 L24 40 Q34 40 34 58 L-40 58 Q-50 58 -50 48 Z"/>
      <path d="M-26 -36 L22 -36 M-26 -26 L22 -26 M-26 -16 L12 -16"/>
      <circle cx="10" cy="6" r="13"/>
      <circle cx="10" cy="6" r="5"/>
      <path d="M2 18 L-2 32 L4 28 L8 34 M18 18 L22 32 L16 28 L12 34"/>
    </g>
    <text class="label label-initial" x="930" y="391">P</text>
    <text class="label label-note" x="985" y="372">(INTELLECTUAL)</text>
    <text class="label label-rest" x="988" y="392">ROPERTY</text>
  </g>

  <!-- Product Clearance -->
  <g class="step step-clearance">
    <circle class="node" cx="882" cy="810" r="88"/>
    <g class="icon" transform="translate(882 810)">
      <rect x="-42" y="-48" width="84" height="104" rx="8"/>
      <rect x="-16" y="-58" width="32" height="16" rx="4"/>
      <circle cx="-20" cy="-18" r="10"/>
      <path d="M-25 -18 L-21 -13 L-14 -23"/>
      <circle cx="-20" cy="10" r="10"/>
      <path d="M-25 10 L-21 15 L-14 5"/>
      <path d="M-2 -22 L30 -22 M-2 -12 L30 -12 M-2 6 L30 6 M-2 16 L30 16 M-30 38 L30 38"/>
    </g>
    <text class="label label-initial" x="1007" y="798">P</text>
    <text class="label label-rest" x="1037" y="800">RODUCT</text>
    <text class="label label-rest" x="1018" y="819">CLEARANCE</text>
  </g>

  <!-- Payment -->
  <g class="step step-payment">
    <circle class="node" cx="612" cy="944" r="88"/>
    <g class="icon" transform="translate(612 944)">
      <rect x="-52" y="-60" width="104" height="58" rx="3"/>
      <rect x="-44" y="-52" width="88" height="42" rx="8"/>
      <circle cx="0" cy="-31" r="15"/>
      <text x="0" y="-24" text-anchor="middle" class="solid" font-family="Archivo Black, sans-serif" font-size="20">$</text>
      <path d="M-58 24 Q-40 12 -20 14 L14 18 Q20 24 12 28 L-10 28"/>
      <path d="M-48 44 Q-20 34 10 40 L50 20 Q58 18 56 26 L14 50 Q0 56 -20 50"/>
    </g>
    <text class="label label-initial" x="555" y="1105">P</text>
    <text class="label label-rest" x="584" y="1106">AYMENT</text>
  </g>

  <!-- Pilots -->
  <g class="step step-pilots">
    <circle class="node" cx="338" cy="810" r="88"/>
    <g class="icon" transform="translate(338 810)">
      <circle class="solid" cx="12" cy="-46" r="6"/>
      <circle class="solid" cx="38" cy="-46" r="6"/>
      <path d="M6 -46 L0 -46 L2 -14 Q6 10 24 10 Q42 10 46 -14 L48 -46 L44 -46"/>
      <path d="M24 10 L24 34 Q24 58 0 58 Q-38 58 -40 34 Q-40 16 -26 4 Q-18 -4 -20 -10"/>
      <circle cx="-30" cy="-20" r="12"/>
      <circle cx="-30" cy="-20" r="4"/>
    </g>
    <text class="label label-initial" x="155" y="761">P</text>
    <text class="label label-rest" x="184" y="762">ILOTS</text>
  </g>

  <!-- Physician and Patient Feedback -->
  <g class="step step-feedback">
    <circle class="node" cx="275" cy="519" r="88"/>
    <g class="icon" transform="translate(275 519)">
      <path d="M-52 -44 Q-52 -52 -44 -52 L18 -52 Q26 -52 26 -44 L26 -6 Q26 2 18 2 L-18 2 L-42 26 L-42 2 L-44 2 Q-52 2 -52 -6 Z"/>
      <path d="M32 -26 L50 -26 Q58 -26 58 -18 L58 20 Q58 28 50 28 L48 28 L48 50 L26 28 L-4 28 Q-10 28 -10 20 L-10 14"/>
      <path class="solid" d="M-13 -12 L-30 -28 Q-38 -38 -30 -44 Q-20 -48 -13 -38 Q-6 -48 4 -44 Q12 -38 4 -28 Z"/>
    </g>
    <text class="label label-initial" x="163" y="366">P</text>
    <text class="label label-rest" x="189" y="367">HYSICIAN</text>
    <text class="label label-rest" x="171" y="392">AND PATIENT</text>
    <text class="label label-rest" x="185" y="416">FEEDBACK</text>
  </g>
</svg>
</body>
</html>
```